Book cover for the book Quiet Rivers Beneath a Morning Gate

This is a 6x9 paperback book titled Quiet Rivers Beneath a Morning Gate: Letters Gathered Across Forty Summers of Garden Walks and Kitchen Talks at Dusk. It will be a cover full of love, reunion, and warmth. No ghosts, cemeteries, and so on. I'm open to any creative design. Might include someone rising in spirit from a sick bed to the welcoming arms of loved ones. Or someone being greeted by family in a scene of enchanting beauty that is the life after this life. The world of the life after this life is just like earth, except more beautiful, with colors we can't imagine, large flowers, opulent buildings, and people all young wearing robes of varying colors. No religious symbols. No sun, moon, or stars.

Font styles to use
Serif

Requirements
Should not have
• Cemeteries, ghosts, anything ghoulish and spooky

```html
<!DOCTYPE html>
<html lang="en">
<head>
<meta charset="utf-8">
<title>Quiet Rivers Beneath a Morning Gate — Cover</title>
<link rel="stylesheet" href="https://fonts.googleapis.com/css2?family=Cinzel:wght@400;500&display=swap">
<style>
  :root {
    --page: #ffffff;
    --ink: #151a2c;
    --ember-dark: #4b1a0b;
    --ember: #e07b26;
    --cream: #fbf3ea;
    --sky-top: #e9e6ee;
    --sky-mid: #f4ebe8;
    --glow: #f7c27a;
    --field: #b7592a;
    --earth: #5a220f;
    --earth-deep: #3f170a;
  }
  html, body {
    margin: 0;
    width: 1200px;
    height: 1200px;
    overflow: hidden;
    background: var(--page);
  }
  .stage {
    position: relative;
    width: 1200px;
    height: 1200px;
  }
  .cover {
    position: absolute;
    left: 274px;
    top: 109px;
    width: 660px;
    height: 989px;
    overflow: hidden;
    border: 2px solid #8e8e8e;
    box-sizing: border-box;
    box-shadow: 0 6px 40px rgba(0,0,0,0.10);
    font-family: "Cinzel", "Times New Roman", serif;
  }
  .cover-art {
    position: absolute;
    inset: 0;
    background:
      radial-gradient(ellipse 55% 30% at 50% 66%, rgba(255,236,190,0.9), rgba(255,236,190,0) 70%),
      linear-gradient(180deg,
        var(--sky-top) 0%,
        var(--sky-mid) 30%,
        #f1e2e0 48%,
        #f5dcc0 60%,
        var(--glow) 68%,
        var(--field) 78%,
        var(--earth) 90%,
        var(--earth-deep) 100%);
  }
  .title-line {
    position: absolute;
    left: 0;
    right: 0;
    margin: 0;
    text-align: center;
    line-height: 1;
    color: var(--ink);
    font-weight: 500;
    white-space: nowrap;
  }
  .title-quiet   { top: 35px;  font-size: 50px; letter-spacing: 1px; }
  .title-rivers  { top: 80px;  font-size: 82px; }
  .title-beneath { top: 159px; font-size: 66px; }
  .title-morning {
    top: 245px;
    font-size: 100px;
    font-weight: 400;
    background: linear-gradient(160deg, var(--ember-dark) 0%, var(--ember-dark) 48%, var(--ember) 48%, var(--ember) 100%);
    -webkit-background-clip: text;
    background-clip: text;
    color: transparent;
  }
  .title-gate    { top: 336px; font-size: 108px; }
  .subtitle {
    position: absolute;
    left: 40px;
    right: 40px;
    top: 900px;
    margin: 0;
    text-align: center;
    font-style: italic;
    font-family: "Cinzel", "Times New Roman", serif;
    font-size: 17px;
    line-height: 31px;
    letter-spacing: 1px;
    color: var(--cream);
    transform: skewX(-10deg);
  }
</style>
</head>
<body>
<main class="stage">
  <section class="cover">
    <div class="cover-art" role="img" aria-label="Photograph of a family embracing in a tall grass field at golden hour beneath soft pink and lavender clouds"></div>
    <h1 class="title">
      <span class="title-line title-quiet">Quiet</span>
      <span class="title-line title-rivers">Rivers</span>
      <span class="title-line title-beneath">Beneath a</span>
      <span class="title-line title-morning">Morning</span>
      <span class="title-line title-gate">Gate</span>
    </h1>
    <p class="subtitle">LETTERS GATHERED ACROSS FORTY SUMMERS OF GARDEN WALKS AND KITCHEN TALKS AT DUSK.</p>
  </section>
</main>
</body>
</html>
```